Billboard Design for Modern Dispensary

Hello!
We need a eye-catching 12' x 24' billboard designed for a very successful, modern cannabis dispensary on the Oregon coast, United States. Because of rules, we cannot have any marijuana leafs or other cannabis related images (flower, joints, smoke, etc). We can use the words "Shop" or "Dispensary" - we cannot use the words "cannabis", "marijuana".

Some ideas we had are 3 words stacked on left or center of billboard - maybe across bottom we have horizontal logo and the following words - “South of bridge in Depoe Bay”
Another idea is to have a small bubble in bottom/top corner with image of our dog (face only) - with some words around it - like "BONUS Shop Dog" or "Cute Shop Dog" or "Best Shop Dog" or "Friendly Staff"

here's some 3 word examples:
ENJOY
YOUR
TRIP

or

FEEL
GOOD
JUST
AHEAD

or

GOOD
VIBES
ONLY

or

GOOD
TIMES
CHILL
VIBES

I have attached our logo. I have also included a stacked logo version (vertical, not horizontal). the formats are .EPS and .PDF - the logos were created in Affinity Design 2.x.

Our website is coralnook.net if you want to see more images, etc about our dispensary.

Artwork Requirements:
The billboard is 12' tall x 25' wide
The artwork needs to be 1”=1’ @ 300dpi
Please add 6” of bleed all around so your total artwork is 13”x26”
Final deliverable should be .Ai file.

Font styles to use
Sans Serif

Colors
0054AA
0677BA
7BADD7
CADEEF
E8F1F8

Requirements
Nice to have
• See the project description - we included some ideas to consider.
Should not have
• No cannabis images, like flower, cannabis leaves, paraphenlia, cartridges, joints, etc.

```html
<!DOCTYPE html>
<html lang="en">
<head>
<meta charset="utf-8">
<title>Coral Nook Billboard</title>
<link rel="stylesheet" href="https://fonts.googleapis.com/css2?family=Arimo:wght@400&family=Open+Sans:wght@700&family=Montserrat:wght@400&display=swap">
<style>
  :root {
    --stage: #0b0b0c;
    --panel-deep: #22679c;
    --panel-bright: #3b9ad6;
    --ring-dark: #2769a6;
    --ring-pale: #c4d5e6;
    --stripe: #ffffff;
    --ink: #111418;
    --mist: #e8f1f8;
    --photo-warm: #c9a673;
    --photo-dark: #3a2a22;
  }
  html, body {
    margin: 0;
    width: 1200px;
    height: 1200px;
    overflow: hidden;
    background: var(--stage);
  }
  .billboard {
    position: absolute;
    left: 50px;
    top: 337px;
    width: 1100px;
    height: 526px;
    display: block;
  }
  .brand-name {
    font-family: "Arimo", Arial, sans-serif;
    font-weight: 400;
    fill: var(--stripe);
  }
  .brand-place {
    font-family: "Arimo", Arial, sans-serif;
    fill: var(--ink);
    letter-spacing: 7px;
  }
  .slogan {
    font-family: "Open Sans", Arial, sans-serif;
    font-weight: 700;
    fill: var(--stripe);
  }
  .web-address {
    font-family: "Montserrat", Arial, sans-serif;
    fill: var(--mist);
    letter-spacing: 3px;
  }
</style>
</head>
<body>
<svg class="billboard" viewBox="0 0 1143 546" xmlns="http://www.w3.org/2000/svg">
  <defs>
    <radialGradient id="shop-dog-tones" cx="50%" cy="45%" r="60%">
      <stop offset="0%" stop-color="var(--photo-warm)"/>
      <stop offset="70%" stop-color="#a88a60"/>
      <stop offset="100%" stop-color="var(--photo-dark)"/>
    </radialGradient>
    <path id="slogan-arc" d="M 677 302 A 190 190 0 1 1 1057 302"/>
  </defs>

  <!-- panels -->
  <rect class="panel-bright" width="1143" height="546" fill="var(--panel-bright)"/>
  <polygon class="panel-deep" points="0,0 575,0 505,546 0,546" fill="var(--panel-deep)"/>
  <polygon class="divider-stripe" points="575,0 582,0 528,546 505,546" fill="var(--stripe)"/>

  <!-- brand block -->
  <g class="brand">
    <circle cx="250" cy="198" r="70" fill="var(--panel-bright)"/>
    <text class="brand-name" x="250" y="330" text-anchor="middle" font-size="62" textLength="370" lengthAdjust="spacingAndGlyphs">CORAL NOOK</text>
    <line x1="68" y1="355" x2="130" y2="355" stroke="var(--ink)" stroke-width="2"/>
    <line x1="357" y1="355" x2="435" y2="355" stroke="var(--ink)" stroke-width="2"/>
    <text class="brand-place" x="247" y="362" text-anchor="middle" font-size="19">DEPOE  BAY</text>
  </g>

  <!-- shop dog badge -->
  <g class="dog-badge">
    <circle cx="867" cy="273" r="148" fill="var(--ring-dark)"/>
    <circle cx="867" cy="273" r="137" fill="var(--panel-bright)"/>
    <circle cx="867" cy="273" r="126" fill="var(--ring-pale)"/>
    <circle cx="867" cy="273" r="118" fill="url(#shop-dog-tones)" role="img" aria-label="Photo of the shop dog, a smiling golden doodle"/>
    <text class="slogan" font-size="42">
      <textPath href="#slogan-arc" startOffset="50%" text-anchor="middle" textLength="590" lengthAdjust="spacingAndGlyphs">BEST • DISPENSARY • PERIOD</textPath>
    </text>
  </g>

  <text class="web-address" x="853" y="463" text-anchor="middle" font-size="21">www.coralnook.net</text>
</svg>
</body>
</html>
```